Business card for my new company (Accounting firm)

I need a business card for my new business Corvane Advisory and Ledger SA. Our services are accounting, tax, audit and financial management. Our customers are small companies, start-ups and new companies. The final design has to show financial security, trust and growth. Please find our logo attached to the business card. Text for the business card: Corvane Advisory and Ledger SA Tomas da Varela Director and Founder Certified Accountant Tel. 022 418 27 35 tv@corvaneconseil.ch www.corvaneconseil.ch Rue des Vergers-Bleus 14 1201 Geneva
Target Market(s)
Our customers are small companies, start-ups and new companies.
Industry/Entity Type
Finance And Accounting
Contact Information for Business Card
Corvane Conseil et Registre SA
Tomas da Varela
Directeur et Fondateur
Expert-comptable diplômé
Tél. 022 418 27 35
tv@corvaneconseil.ch
www.corvaneconseil.ch
Rue des Vergers-Bleus 14
1201 Genève

```html
<!DOCTYPE html>
<html lang="fr">
<head>
<meta charset="utf-8">
<title>Corvane Conseil et Registre SA – Carte de visite</title>
<link rel="stylesheet" href="https://fonts.googleapis.com/css2?family=Lato:wght@400;700&family=Montserrat:wght@600&display=swap">
<style>
  :root {
    --bg: #17181b;
    --brand-blue: #1b6696;
    --sky-blue: #2aa9e0;
    --ink: #3a3a3c;
    --paper: #ffffff;
  }
  * { box-sizing: border-box; margin: 0; padding: 0; }
  html, body { width: 1200px; height: 912px; overflow: hidden; background: var(--bg); }
  .canvas {
    width: 1200px; height: 912px;
    display: flex; flex-direction: column; align-items: center; justify-content: center; gap: 48px;
  }
  .card {
    position: relative; width: 640px; height: 388px; overflow: hidden;
    box-shadow: 0 14px 30px rgba(0,0,0,.45);
    font-family: "Lato", sans-serif;
  }
  /* front */
  .card-front { background: var(--brand-blue); color: var(--paper); }
  .front-brand {
    position: absolute; left: 0; right: 0; top: 130px;
    display: flex; align-items: center; justify-content: center; gap: 14px;
  }
  .brand-square { width: 26px; height: 26px; background: var(--paper); }
  .front-brand .brand-name {
    font-family: "Montserrat", sans-serif; font-weight: 600; font-size: 58px; letter-spacing: 2px;
  }
  .front-web {
    position: absolute; left: 0; right: 0; top: 262px; text-align: center; font-size: 19px;
  }
  /* back */
  .card-back { background: var(--paper); color: var(--ink); }
  .back-brand {
    position: absolute; left: 48px; top: 150px;
    display: flex; align-items: center; gap: 12px;
  }
  .back-brand .brand-square { background: var(--brand-blue); width: 22px; height: 22px; }
  .back-brand .brand-name {
    font-family: "Montserrat", sans-serif; font-weight: 600; font-size: 44px; letter-spacing: 1px; color: var(--ink);
  }
  .divider {
    position: absolute; left: 48px; right: 40px; top: 222px; height: 1.5px; background: var(--brand-blue);
  }
  .person {
    position: absolute; right: 40px; top: 40px; text-align: right; line-height: 1.3;
  }
  .person-name { color: var(--brand-blue); font-weight: 700; font-size: 24px; }
  .person-role { font-size: 16px; }
  .company {
    position: absolute; right: 40px; top: 128px; text-align: right; font-size: 16px; line-height: 1.3;
  }
  .contact {
    position: absolute; left: 48px; top: 240px; font-size: 19px; line-height: 1.45;
  }
  .contact-row { display: flex; align-items: center; gap: 10px; }
  .contact-row svg { width: 16px; height: 16px; fill: var(--brand-blue); }
  .band { position: absolute; left: 0; top: 0; width: 640px; height: 388px; }
  .back-web {
    position: absolute; right: 40px; top: 326px; color: var(--paper); font-size: 18px;
  }
</style>
</head>
<body>
<main class="canvas">
  <section class="card card-front" aria-label="Recto">
    <div class="front-brand">
      <span class="brand-square"></span>
      <span class="brand-name">Corvane</span>
    </div>
    <p class="front-web">www.corvaneconseil.ch</p>
  </section>

  <section class="card card-back" aria-label="Verso">
    <svg class="band" viewBox="0 0 640 388" aria-hidden="true">
      <path d="M360 388 L400 360 C412 352 414 320 428 304 L640 284 L640 388 Z" fill="var(--brand-blue)"/>
      <path d="M0 356 L384 334 C404 332 410 316 420 298 L428 304 C414 320 412 352 400 360 L360 388 L0 388 Z" fill="var(--sky-blue)"/>
      <path d="M0 366 L392 344 C408 342 414 330 420 312" fill="none" stroke="var(--paper)" stroke-width="3"/>
      <rect x="0" y="378" width="640" height="10" fill="var(--sky-blue)"/>
    </svg>

    <div class="person">
      <p class="person-name">Tomas da Varela</p>
      <p class="person-role">Directeur et Fondateur</p>
      <p class="person-role">Expert-comptable diplômé</p>
    </div>

    <div class="company">
      <p>Corvane Conseil et Registre SA</p>
      <p>Rue des Vergers-Bleus 14</p>
      <p>1201 Genève</p>
    </div>

    <div class="back-brand">
      <span class="brand-square"></span>
      <span class="brand-name">Corvane</span>
    </div>

    <div class="divider"></div>

    <div class="contact">
      <p class="contact-row">
        <svg viewBox="0 0 24 24" aria-hidden="true"><path d="M6.6 10.8a15 15 0 0 0 6.6 6.6l2.2-2.2a1 1 0 0 1 1-.25 11.4 11.4 0 0 0 3.6.57 1 1 0 0 1 1 1V20a1 1 0 0 1-1 1A17 17 0 0 1 3 4a1 1 0 0 1 1-1h3.5a1 1 0 0 1 1 1c0 1.25.2 2.45.57 3.57a1 1 0 0 1-.25 1z"/></svg>
        <span>022 418 27 35</span>
      </p>
      <p class="contact-row">
        <svg viewBox="0 0 24 24" aria-hidden="true"><path d="M2 5h20v14H2z M3.5 6.5 12 13l8.5-6.5" fill="var(--brand-blue)" stroke="var(--paper)" stroke-width="1.2"/></svg>
        <span>tv@corvaneconseil.ch</span>
      </p>
    </div>

    <p class="back-web">www.corvaneconseil.ch</p>
  </section>
</main>
</body>
</html>
```